Bref créative
Business Card for financial advisor
RVT Advisory Partners
Simple
Irina Lebedinskaya
Director
42 Marlow Yard
London
SW9 3QT
irina.lebedinskaya@rvtsupport.example

```html
<!DOCTYPE html>
<html lang="en">
<head>
<meta charset="utf-8">
<title>RVT Advisory Partners – Business Card</title>
<link rel="stylesheet" href="https://fonts.googleapis.com/css2?family=Roboto:wght@400;500;700&display=swap">
<style>
  :root {
    --bg: #e9eaec;
    --card: #ffffff;
    --red: #d9232e;
    --grey: #5b5c5e;
    --grey-dark: #333436;
    --grey-light: #c9cacc;
  }
  * { margin: 0; padding: 0; box-sizing: border-box; }
  html, body {
    width: 1200px; height: 1009px; overflow: hidden;
    background: var(--bg);
    font-family: "Roboto", Arial, sans-serif;
  }
  .sheet {
    width: 1200px; height: 1009px;
    display: flex; flex-direction: column; align-items: center; justify-content: center;
    gap: 40px;
  }
  .card {
    position: relative;
    width: 770px; height: 440px;
    background: var(--card);
    border-radius: 22px;
    overflow: hidden;
    box-shadow: 0 6px 18px rgba(0,0,0,.12);
  }
  .brand { display: flex; align-items: center; gap: 14px; }
  .brand-mark { width: 28px; height: 28px; background: var(--red); flex: none; }
  .brand-name { font-weight: 700; color: var(--grey-dark); line-height: 1; white-space: nowrap; }

  /* front */
  .card-front .brand { position: absolute; left: 54px; top: 130px; }
  .card-front .brand-name { font-size: 28px; }
  .contact {
    position: absolute; left: 420px; top: 120px;
    border-left: 1px solid var(--grey-light);
    padding-left: 22px;
  }
  .contact-name { color: var(--red); font-size: 24px; font-weight: 500; }
  .contact-role { color: var(--grey); font-size: 16px; margin-top: 4px; margin-bottom: 18px; }
  .contact-line {
    display: flex; align-items: center; gap: 10px;
    color: var(--grey-dark); font-size: 14px; line-height: 1; margin-bottom: 9px;
  }
  .contact-line svg { width: 14px; height: 14px; flex: none; fill: var(--red); }
  .contact-line .spacer { width: 14px; flex: none; }
  .swoosh { position: absolute; left: 0; bottom: 0; width: 770px; height: 170px; }

  /* back */
  .card-back { display: flex; align-items: center; justify-content: center; }
  .card-back .brand { gap: 18px; }
  .card-back .brand-mark { width: 46px; height: 46px; }
  .card-back .brand-name { font-size: 48px; }
</style>
</head>
<body>
<main class="sheet">
  <section class="card card-front">
    <div class="brand">
      <span class="brand-mark"></span>
      <span class="brand-name">RVT Advisory Partners</span>
    </div>
    <div class="contact">
      <p class="contact-name">Irina Lebedinskaya</p>
      <p class="contact-role">Director</p>
      <p class="contact-line">
        <svg viewBox="0 0 24 24"><path d="M12 2a7 7 0 0 0-7 7c0 5 7 13 7 13s7-8 7-13a7 7 0 0 0-7-7zm0 9.5A2.5 2.5 0 1 1 12 6.5a2.5 2.5 0 0 1 0 5z"/></svg>
        42 Marlow Yard, London
      </p>
      <p class="contact-line"><span class="spacer"></span>SW9 3QT</p>
      <p class="contact-line">
        <svg viewBox="0 0 24 24"><path d="M6.6 10.8a15 15 0 0 0 6.6 6.6l2.2-2.2a1 1 0 0 1 1-.25 11.4 11.4 0 0 0 3.6.57 1 1 0 0 1 1 1V20a1 1 0 0 1-1 1A17 17 0 0 1 3 4a1 1 0 0 1 1-1h3.5a1 1 0 0 1 1 1c0 1.25.2 2.45.57 3.57a1 1 0 0 1-.25 1z"/></svg>
        +44 (0) 208 555 0142
      </p>
      <p class="contact-line">
        <svg viewBox="0 0 24 24"><path d="M16 1H8a2 2 0 0 0-2 2v18a2 2 0 0 0 2 2h8a2 2 0 0 0 2-2V3a2 2 0 0 0-2-2zm-4 21a1.3 1.3 0 1 1 0-2.6 1.3 1.3 0 0 1 0 2.6zM16 18H8V4h8z"/></svg>
        +44 (0) 770 090 0317
      </p>
      <p class="contact-line">
        <svg viewBox="0 0 24 24"><path d="M20 4H4a2 2 0 0 0-2 2v12a2 2 0 0 0 2 2h16a2 2 0 0 0 2-2V6a2 2 0 0 0-2-2zm0 4-8 5-8-5V6l8 5 8-5z"/></svg>
        irina.lebedinskaya@rvtsupport.example
      </p>
    </div>
    <svg class="swoosh" viewBox="0 0 770 170" preserveAspectRatio="none" aria-hidden="true">
      <path d="M0 40 C 180 70, 300 140, 770 150 L770 170 L0 170 Z" fill="var(--grey-light)"/>
      <path d="M0 60 C 170 95, 300 150, 770 158 L770 170 L0 170 Z" fill="var(--grey)"/>
      <path d="M0 78 C 170 115, 300 160, 770 164 L770 170 L0 170 Z" fill="var(--red)"/>
    </svg>
  </section>

  <section class="card card-back">
    <div class="brand">
      <span class="brand-mark"></span>
      <span class="brand-name">RVT Advisory Partners</span>
    </div>
  </section>
</main>
</body>
</html>
```